Business card for Financial Technology company

Hello! We'd like to create business cards for 4 members of our company. Our company is a financial technology business that provides funding for businesses. We want to give it a VC (venture captal) look and feel. Clean, fresh and minimal but with a flair of artistry. I'll include some samples of cards we like. It would be great if the back of the card was artistic (see sample files 1 and 2) and the front of the card was the business info. The name of the company is Q7 Funding.

```html
<!DOCTYPE html>
<html lang="en">
<head>
<meta charset="utf-8">
<title>Q7 Funding — Business Card</title>
<link href="https://fonts.googleapis.com/css2?family=Poppins:wght@400;500;600&display=swap" rel="stylesheet">
<style>
  :root {
    --backdrop: #c4c4c4;
    --card-light: #ffffff;
    --card-dark: #000000;
    --brand-green: #2e9e48;
    --ink: #2b2b2b;
    --rule: #8a8a8a;
    --on-dark: #ffffff;
    --art-lime: #9bbd3c;
    --art-green: #0a8a45;
    --art-teal: #15566b;
    --art-indigo: #3a2a7a;
    --art-magenta: #d0188a;
    --art-coral: #ee5560;
    --art-amber: #f6a12a;
  }
  * { margin: 0; padding: 0; box-sizing: border-box; }
  html, body {
    width: 1093px; height: 1200px; overflow: hidden;
    background: var(--backdrop);
    font-family: "Poppins", sans-serif;
  }
  .card {
    position: absolute;
    left: 264px;
    width: 580px;
    height: 358px;
    overflow: hidden;
  }
  .card-front { top: 226px; background: var(--card-light); color: var(--ink); }
  .card-back { top: 620px; height: 361px; background: var(--card-dark); }

  .brand-mark {
    position: absolute;
    left: 68px; top: 160px;
    display: flex; align-items: center; gap: 10px;
  }
  .brand-square {
    width: 22px; height: 22px;
    background: var(--brand-green);
  }
  .brand-name {
    font-size: 26px; font-weight: 600;
    color: var(--brand-green);
  }
  .divider {
    position: absolute;
    left: 289px; top: 75px;
    width: 1px; height: 208px;
    background: var(--rule);
  }
  .contact {
    position: absolute;
    left: 307px; top: 90px;
  }
  .person-name {
    font-size: 25px; font-weight: 500;
    color: var(--brand-green);
    line-height: 1;
  }
  .person-role {
    font-size: 17px; line-height: 1.1;
    margin-top: 1px;
  }
  .contact-list {
    list-style: none;
    margin-top: 14px;
  }
  .contact-list li {
    display: flex; align-items: center; gap: 7px;
    font-size: 17px; line-height: 21px;
  }
  .contact-list svg { width: 15px; height: 15px; flex: none; }
  .address {
    font-style: normal;
    font-size: 17px; line-height: 21px;
    margin-top: 13px;
  }

  .back-artwork {
    position: absolute;
    left: 0; top: 8px;
    width: 220px; height: 348px;
    background: linear-gradient(160deg,
      var(--art-lime) 0%,
      var(--art-green) 28%,
      var(--art-teal) 44%,
      var(--art-indigo) 60%,
      var(--art-magenta) 78%,
      var(--art-coral) 88%,
      var(--art-amber) 100%);
    opacity: 0.9;
  }
  .back-name {
    position: absolute;
    left: 278px; top: 252px;
    font-size: 46px; font-weight: 600;
    color: var(--on-dark);
    line-height: 1;
  }
</style>
</head>
<body>
  <section class="card card-front">
    <div class="brand-mark">
      <span class="brand-square"></span>
      <span class="brand-name">Q7 Funding</span>
    </div>
    <div class="divider"></div>
    <div class="contact">
      <h1 class="person-name">Marcus Ellery</h1>
      <p class="person-role">Managing Director</p>
      <ul class="contact-list">
        <li>
          <svg viewBox="0 0 16 16" aria-hidden="true"><path d="M3 1.5l2.6 0 1 3.2-1.6 1.3c.8 1.8 2.2 3.2 4 4l1.3-1.6 3.2 1v2.6c0 .8-.7 1.5-1.5 1.4C6.6 13 3 9.4 1.6 3c-.1-.8.6-1.5 1.4-1.5z" fill="none" stroke="var(--brand-green)" stroke-width="1.5"/><path d="M9.5 2.5a4 4 0 0 1 4 4M9.5 5a1.6 1.6 0 0 1 1.6 1.6" fill="none" stroke="var(--brand-green)" stroke-width="1.3"/></svg>
          044-555 210 376
        </li>
        <li>
          <svg viewBox="0 0 16 16" aria-hidden="true"><rect x="0.5" y="3" width="15" height="10" fill="var(--brand-green)"/><path d="M1 3.5l7 5.5 7-5.5M1 12.5l5-4.5M15 12.5l-5-4.5" fill="none" stroke="#fff" stroke-width="1"/></svg>
          hello@q7funding.com
        </li>
        <li>
          <svg viewBox="0 0 16 16" aria-hidden="true"><g fill="none" stroke="var(--brand-green)" stroke-width="1.3"><circle cx="8" cy="8" r="6.8"/><ellipse cx="8" cy="8" rx="3" ry="6.8"/><path d="M1.2 8h13.6M2.5 4.5h11M2.5 11.5h11"/></g></svg>
          www.q7funding.com
        </li>
      </ul>
      <address class="address">421, Address line goes here<br>45452,Country Name</address>
    </div>
  </section>

  <section class="card card-back">
    <div class="back-artwork" role="img" aria-label="Large multicolour brand artwork in green, teal, purple, magenta and amber"></div>
    <h2 class="back-name">Q7 Funding</h2>
  </section>
</body>
</html>
```